Website Landing Page for Medical Recruitment

Looking for a landing page to add to our existing website. The objective of the page is to recruit new clinical staff for various departments within Larkfield Medical Center (non-profit hospital in the Richmond, TX area).

We would like the page to be modern, professional, and non-cluttered. Please include call-to-actions and include a button that will navigate to the page where candidates can submit their applications (this page already exists).

Target Market(s)

25-35-year-olds who live in the Houston and Richmond area with medical experience.

Industry/Entity Type

Medical/Health

Font styles to use
Sans Serif

Colors
0054AA
0677BA
7BADD7
CADEEF
E8F1F8

Requirements
Must have
• A "call to action"; a button that navigates to larkfieldmedhub.example/careers

```html
<!DOCTYPE html>
<html lang="en">
<head>
<meta charset="utf-8">
<title>Larkfield Medical Center — Careers</title>
<link href="https://fonts.googleapis.com/css2?family=Cinzel:wght@500;600&family=Roboto:wght@400;500;700&display=swap" rel="stylesheet">
<style>
:root{
  --navy:#23498c;
  --navy-deep:#1c3d78;
  --blue:#0054AA;
  --sky:#7BADD7;
  --pale:#CADEEF;
  --mist:#E8F1F8;
  --ink:#1f2024;
  --dark:#1d1d1f;
  --text:#8a8d93;
  --grey-bg:#f3f4f6;
  --white:#ffffff;
}
*{box-sizing:border-box;margin:0;padding:0}
html,body{width:1200px;height:4295px;overflow:hidden}
body{position:relative;background:var(--white);font-family:"Roboto",sans-serif;color:var(--ink)}
.abs{position:absolute}
a{text-decoration:none;color:inherit}
.btn{position:absolute;display:flex;align-items:center;justify-content:center;border-radius:30px;background:var(--navy);color:var(--white);font-weight:700;font-size:14px;text-transform:uppercase;letter-spacing:.2px}
.serif{font-family:"Cinzel",serif;font-weight:600;letter-spacing:1px}
.serif .soft{color:#8f929a}
.photo{position:absolute;overflow:hidden}

/* top bar */
.topbar{top:0;left:0;width:1200px;height:42px;background:var(--dark)}
.topbar-contact{top:0;left:0;width:497px;height:42px;background:var(--navy);display:flex;align-items:center;padding-left:110px;gap:26px;color:#dfe6f2;font-size:13px}
.socials{display:flex;gap:8px}
.social{width:32px;height:32px;border-radius:50%;border:1.5px solid #fff}
.social.fill{background:var(--navy);border-color:var(--navy)}

/* header */
.brand{display:flex;align-items:center;gap:10px;color:var(--navy);font-size:20px;font-weight:500;white-space:nowrap}
.brand-dot{width:36px;height:36px;border-radius:50%;background:var(--navy);flex:none}
.nav{top:80px;left:415px;display:flex;gap:24px;font-size:13px;font-weight:500;color:#2a2c31}
.nav .active{color:var(--navy);border-bottom:2px solid var(--navy);padding-bottom:3px}

/* paragraphs */
.copy{font-size:14.5px;line-height:26px;color:var(--text);text-align:justify}
.copy p+p{margin-top:12px}
.sec-title{font-size:38px}
.bar-title{padding-left:22px;border-left:3px solid var(--navy);line-height:34px}
.center-title{left:0;width:1200px;text-align:center}
.divider{left:530px;width:140px;display:flex;align-items:center;justify-content:space-between}
.divider i{width:48px;height:2px;background:#9aa0aa}
.divider b{width:22px;height:22px;border-radius:50%;background:var(--navy)}

/* offer cards */
.card{position:absolute;top:1552px;width:310px;height:433px;background:#fff;border-radius:8px;box-shadow:0 4px 18px rgba(30,50,90,.14);text-align:center}
.card .photo{left:8px;top:5px;width:294px;height:210px;border-radius:4px}
.card h3{position:absolute;top:240px;left:0;width:100%;font-size:15px;font-weight:500}
.card h3::after{content:"";display:block;width:48px;height:3px;background:var(--navy);margin:9px auto 0}
.card p{position:absolute;top:282px;left:22px;width:266px;font-size:13px;line-height:23px;color:var(--text)}
.card .btn{top:370px;left:97px;width:115px;height:38px;font-size:11px}
.arrow{position:absolute;top:1750px}

/* resources */
.res{position:absolute;background:#fff;box-shadow:0 4px 18px rgba(30,50,90,.13)}
.date{display:flex;align-items:center;gap:10px;font-size:11px;color:#444}
.date b{width:22px;height:22px;border-radius:50%;background:var(--navy)}
.res h4{font-size:16px;font-weight:700;line-height:24px;text-transform:uppercase}
.res p{font-size:13.5px;line-height:25px;color:var(--text)}
.more{display:flex;align-items:center;gap:8px;color:var(--navy);font-size:13.5px;font-weight:700}
.more i{width:13px;height:13px;border-radius:50%;background:var(--navy)}

/* contact */
.field{position:absolute;background:#fff;border:1px solid #e3e5ea;border-radius:6px;font-size:14px;color:#777;padding:16px 17px}

/* footer */
.foot-nav{top:4135px;left:0;width:1200px;display:flex;justify-content:center;gap:20px;color:#fff;font-size:15px;font-weight:500}
.foot-line{left:0;width:1200px;text-align:center;color:#e8e8ea;font-size:14.5px}
</style>
</head>
<body>

<!-- top bar -->
<div class="abs topbar"></div>
<div class="abs topbar-contact"><span>&#9742;&nbsp; 281-555-0142</span><span>|</span><span>&#9993;&nbsp; jobs@larkfieldmed.example</span></div>
<div class="abs socials" style="top:5px;left:928px"><span class="social fill"></span><span class="social"></span><span class="social"></span><span class="social"></span></div>

<!-- header -->
<a class="abs brand" style="top:72px;left:110px" href="#"><span class="brand-dot"></span>Larkfield Medical Center</a>
<nav class="abs nav"><span class="active">HOME</span><span>ABOUT US</span><span>SERVICES</span><span>CAREERS</span><span>RESOURCES</span><span>CONTACT US</span></nav>
<a class="btn" style="top:65px;left:955px;width:133px;height:50px;font-size:15px" href="https://larkfieldmedhub.example/careers">Apply Now</a>

<!-- hero -->
<div class="photo" role="img" aria-label="Nurse in blue scrubs working on a laptop at a bright clinic desk" style="top:135px;left:0;width:1200px;height:640px;background:linear-gradient(100deg,#8fa7c4 0%,#c9d3de 35%,#e9ecef 65%,#dfe2e5 100%)"></div>
<svg class="abs" style="top:600px;left:0" width="1200" height="200" viewBox="0 0 1200 200">
  <path d="M0 40 C200 180 420 190 650 120 C860 55 1050 40 1200 75 L1200 200 L0 200Z" fill="var(--navy)"/>
  <path d="M0 60 C200 185 420 185 640 125 C860 65 1050 65 1200 105 L1200 200 L0 200Z" fill="#fff"/>
</svg>
<h1 class="abs serif" style="top:328px;left:620px;font-size:35px;line-height:42px;color:#1d1f24">WE ARE LOOKING<br>TO HIRE CLINICAL STAFF</h1>
<a class="btn" style="top:435px;left:620px;width:145px;height:50px;font-size:14px" href="https://larkfieldmedhub.example/careers">Get Started</a>
<svg class="abs" style="top:350px;left:1130px" width="30" height="190">
  <circle cx="15" cy="18" r="12" fill="var(--navy)"/><circle cx="15" cy="18" r="4" fill="#fff"/>
  <circle cx="15" cy="42" r="3.5" fill="#1d1f24"/><circle cx="15" cy="65" r="3.5" fill="#1d1f24"/>
  <rect x="14" y="90" width="2" height="95" fill="var(--navy)"/>
</svg>

<!-- about -->
<div class="abs" style="top:1100px;left:0;width:1200px;height:1000px;background:var(--grey-bg)"></div>
<svg class="abs" style="top:760px;left:0" width="1200" height="620"><ellipse cx="600" cy="180" rx="1000" ry="430" fill="#fff"/></svg>
<h2 class="abs serif sec-title bar-title" style="top:853px;left:110px">ABOUT <span class="soft">US</span></h2>
<div class="abs copy" style="top:916px;left:110px;width:490px">
  <p>Lorem ipsum dolor sit amet consectetur adipiscing elit, sed do eiusmod tempor incididunt ut labore et dolore magna aliqua. Ut enim ad minim veniam, quis nostrud exercitation ullamco laboris nisi ut aliquip ex ea commodo consequat duis aute irure.</p>
  <p>Sed dolore laboris nisi ut aliquip ex ea commodo consequat duis aute irure dolor in reprehenderit in voluptate velit esse cillum dolore eu fugiat nulla pariuip ex ea commodo consatur.</p>
</div>
<a class="btn" style="top:1142px;left:110px;width:145px;height:50px" href="#">Learn More</a>
<svg class="abs" style="top:815px;left:655px" width="440" height="420">
  <path d="M230 6 A204 204 0 0 1 240 412" fill="none" stroke="var(--navy)" stroke-width="4"/>
</svg>
<div class="photo" role="img" aria-label="Smiling nurse with arms crossed in a clinic" style="top:818px;left:658px;width:410px;height:410px;border-radius:50%;background:radial-gradient(circle at 55% 60%,#5c86c6 0%,#b9c6d6 45%,#e3e7ec 100%)"></div>

<!-- what we offer -->
<h2 class="abs serif sec-title center-title" style="top:1445px">WHAT <span class="soft">WE OFFER</span></h2>
<div class="abs divider" style="top:1497px"><i></i><b></b><i></i></div>
<svg class="arrow" style="left:38px" width="24" height="36"><path d="M18 4 L6 18 L18 32" fill="none" stroke="#9aa0aa" stroke-width="3"/></svg>
<svg class="arrow" style="left:1135px" width="24" height="36"><path d="M6 4 L18 18 L6 32" fill="none" stroke="#1d1f24" stroke-width="3"/></svg>

<div class="card" style="left:110px">
  <div class="photo" role="img" aria-label="Nursing assistant helping an elderly woman walk" style="background:linear-gradient(135deg,#6b6a66 0%,#b7b2a8 55%,#3a5f9e 100%)"></div>
  <h3>CERTIFIED NURSES ASSISTANTS</h3>
  <p>At vero eos et accusamus et iusto odio dignis simos ducimus qui blanditiis praesentium voluptatum deleniti atquea.</p>
  <a class="btn" href="#">Read More</a>
</div>
<div class="card" style="left:445px">
  <div class="photo" role="img" aria-label="Emergency room technicians checking a patient monitor" style="background:linear-gradient(135deg,#c9d2dc,#7f8c99 50%,#2f4f86)"></div>
  <h3>EMERGENCY ROOM TECHS</h3>
  <p>At vero eos et accusamus et iusto odio dignis simos ducimus qui blanditiis praesentium voluptatum deleniti atquea.</p>
  <a class="btn" href="#">Read More</a>
</div>
<div class="card" style="left:780px">
  <div class="photo" role="img" aria-label="Registered nurse with a tablet talking to an older patient" style="background:linear-gradient(135deg,#a89a86,#d9d4ca 50%,#3b64a8)"></div>
  <h3>REGISTERED NURSES</h3>
  <p>At vero eos et accusamus et iusto odio dignis simos ducimus qui blanditiis praesentium voluptatum deleniti atquea.</p>
  <a class="btn" href="#">Read More</a>
</div>

<!-- careers -->
<svg class="abs" style="top:2070px;left:0" width="1200" height="680" viewBox="0 0 1200 680">
  <rect width="1200" height="680" fill="var(--grey-bg)"/>
  <path d="M0 145 C300 -40 900 -40 1200 145 L1200 540 C900 730 300 730 0 540Z" fill="var(--navy)"/>
</svg>
<div class="photo" role="img" aria-label="Smiling nurse with stethoscope in blue scrubs" style="top:2205px;left:110px;width:410px;height:400px;border-radius:50% 30% 50% 50%;background:linear-gradient(120deg,#c6a488 0%,#7c7fa0 40%,#2e58a6 75%,#24498c 100%);opacity:.85"></div>
<h2 class="abs serif sec-title bar-title" style="top:2222px;left:600px;color:#fff;border-color:#fff">CAREERS</h2>
<div class="abs copy" style="top:2286px;left:600px;width:490px;color:#e4e9f2">
  <p>Lorem ipsum dolor sit amet consectetur adipiscing elit, sed do eiusmod tempor incididunt ut labore et dolore magna aliqua. Ut enim ad minim veniam, quis nostrud exercitation ullamco laboris nisi ut aliquip ex ea commodo consequat dmod tempor incididmod tempor incididunt ut labore et dolunt ut labore et doluis aute irure.</p>
  <p>Ullamco laboris nisi ut aliquip ex ea commodo consequat duis aute irure dolor in reprehenderit in voluptate velit esse cillum dolore eu fugiat nulla pariuip ex ea commodo consatur.</p>
</div>
<a class="btn" style="top:2540px;left:600px;width:137px;height:50px;background:#fff;color:var(--ink)" href="https://larkfieldmedhub.example/careers">Apply Now</a>

<!-- resources -->
<h2 class="abs serif sec-title center-title" style="top:2815px">OUR <span class="soft">RESOURCES</span></h2>
<div class="abs divider" style="top:2868px"><i></i><b></b><i></i></div>

<div class="res" style="top:2920px;left:110px;width:480px;height:448px">
  <div class="photo" role="img" aria-label="Nurse sharing a laugh with an elderly woman" style="top:10px;left:10px;width:463px;height:280px;background:linear-gradient(120deg,#8f8a80,#d7cfc2 45%,#5a86c8)"></div>
  <div class="abs date" style="top:310px;left:30px"><b></b>01 JAN 2022</div>
  <h4 class="abs" style="top:347px;left:30px;width:420px">Lorem ipsum dolor sit amet consectetur adi piscing elit sed do eiusmod</h4>
  <a class="abs more" style="top:408px;left:30px" href="#">READ MORE <i></i></a>
</div>
<div class="res" style="top:2920px;left:608px;width:480px;height:213px">
  <div class="photo" role="img" aria-label="Masked doctor at a desk with a phone and laptop" style="top:10px;left:10px;width:197px;height:193px;background:linear-gradient(130deg,#dfe3e8,#8796a8 55%,#2d4f8f)"></div>
  <div class="abs date" style="top:25px;left:227px"><b></b>01 JAN 2022</div>
  <h4 class="abs" style="top:60px;left:227px;width:230px">Lorem ipsum dolor sit amet consec</h4>
  <p class="abs" style="top:113px;left:227px;width:235px">Sed dolore laboris nisi ut aliquip ex ea commodo consequat</p>
  <a class="abs more" style="top:172px;left:227px" href="#">READ MORE <i></i></a>
</div>
<div class="res" style="top:3153px;left:608px;width:480px;height:213px">
  <div class="photo" role="img" aria-label="Surgical team adjusting an IV drip in an operating room" style="top:10px;left:10px;width:197px;height:193px;background:linear-gradient(130deg,#cfd8e2,#5f86b8 50%,#1f4a7a)"></div>
  <div class="abs date" style="top:25px;left:227px"><b></b>01 JAN 2022</div>
  <h4 class="abs" style="top:60px;left:227px;width:230px">Lorem ipsum dolor sit amet consec</h4>
  <p class="abs" style="top:113px;left:227px;width:235px">Sed dolore laboris nisi ut aliquip ex ea commodo consequat</p>
  <a class="abs more" style="top:172px;left:227px" href="#">READ MORE <i></i></a>
</div>

<!-- contact -->
<svg class="abs" style="top:3450px;left:0" width="1200" height="560" viewBox="0 0 1200 560">
  <path d="M0 160 C300 20 900 20 1200 160 L1200 560 L0 560Z" fill="var(--grey-bg)"/>
</svg>
<h2 class="abs serif sec-title center-title" style="top:3532px">CONTACT <span class="soft">US</span></h2>
<div class="abs divider" style="top:3584px"><i></i><b></b><i></i></div>
<div class="field" style="top:3640px;left:165px;width:283px;height:50px">Full Name</div>
<div class="field" style="top:3640px;left:458px;width:283px;height:50px">Phone</div>
<div class="field" style="top:3640px;left:751px;width:283px;height:50px">Email Address</div>
<div class="field" style="top:3700px;left:165px;width:869px;height:95px">Message</div>
<a class="btn" style="top:3808px;left:520px;width:160px;height:48px" href="#">Send Message</a>

<!-- footer -->
<svg class="abs" style="top:3920px;left:0" width="1200" height="375" viewBox="0 0 1200 375">
  <path d="M0 70 C300 150 700 80 950 30 C1060 10 1150 20 1200 40 L1200 375 L0 375Z" fill="var(--navy)"/>
  <path d="M0 110 C300 160 700 110 950 70 C1060 55 1150 60 1200 75 L1200 375 L0 375Z" fill="var(--dark)"/>
</svg>
<div class="abs" style="top:4055px;left:0;width:1200px;display:flex;justify-content:center">
  <span class="brand" style="color:#fff;font-size:22px"><span class="brand-dot" style="background:#fff"></span>Larkfield Medical Center</span>
</div>
<nav class="abs foot-nav"><span>HOME</span><span>|</span><span>ABOUT US</span><span>|</span><span>SERVICES</span><span>|</span><span>CAREERS</span><span>|</span><span>RESOURCES</span><span>|</span><span>CONTACT US</span></nav>
<div class="abs foot-line" style="top:4175px"><span style="color:var(--sky)">&#9679;</span>&nbsp; Maple Row Hospital Campus 2210 Maple Row, Richmond Texas 77400</div>
<div class="abs foot-line" style="top:4206px"><span style="color:var(--sky)">&#9742;</span>&nbsp; 281-555-0142 &nbsp;&nbsp;&nbsp;|&nbsp;&nbsp;&nbsp; <span style="color:var(--sky)">&#9993;</span>&nbsp; jobs@larkfieldmed.example</div>
<div class="abs" style="top:4240px;left:110px;width:980px;height:1px;background:#3a3b40"></div>
<div class="abs foot-line" style="top:4260px;font-size:11px">&copy; 2022 <b>LARKFIELD MEDICAL CENTER</b> &nbsp;·&nbsp; All Rights Reserved</div>
<div class="abs socials" style="top:4252px;left:965px;transform:scale(.85);transform-origin:left top"><span class="social fill"></span><span class="social"></span><span class="social"></span><span class="social"></span></div>

</body>
</html>
```